Harbor Kindness Fund - New Website Design

I need a site that looks like this http://wheelgift-relief.org for boat donations. So please replace the cars with boats.

```html
<!DOCTYPE html>
<html lang="en">
<head>
<meta charset="utf-8">
<title>Harbor Kindness Fund – Donate Boat to Charity</title>
<link href="https://fonts.googleapis.com/css2?family=Bitter:wght@400;500;700&family=Lato:wght@400;700&display=swap" rel="stylesheet">
<style>
:root{
  --gold:#ad9158;
  --gold-dark:#9a7f48;
  --ink:#2b2b2b;
  --black:#0b0b0b;
  --cream:#e8e1d2;
  --hero-light:#efe7cf;
  --hero-dark:#d8ccab;
  --line:#9d9d9d;
  --field:#ffffff;
  --acc-bg:#e6e6e6;
  --footer:#e9e9e9;
}
*{margin:0;padding:0;box-sizing:border-box}
html,body{width:784px;height:1200px;overflow:hidden;background:#fff}
body{position:relative;font-family:"Lato",sans-serif;color:var(--ink)}
.abs{position:absolute}
.serif{font-family:"Bitter",serif}

/* header */
.site-header{position:absolute;left:0;top:0;width:784px;height:62px;background:#fff;border-top:2px solid #222}
.brand{left:152px;top:13px;display:flex;align-items:center;gap:6px}
.brand-mark{width:12px;height:12px;background:var(--gold)}
.brand-name{font-family:"Lato",sans-serif;font-size:10.5px;line-height:10px;color:var(--gold-dark)}
.call{left:403px;top:19px;width:142px;display:flex;align-items:center;gap:5px;font-family:"Bitter",serif;font-size:12px;line-height:18px;color:var(--ink);white-space:nowrap}
.call-icon{flex:none;width:17px;height:17px;border-radius:50%;background:var(--gold);display:flex;align-items:center;justify-content:center}
.donate-btn{left:552px;top:20px;width:81px;height:18px;background:var(--gold-dark);color:#fff;font-size:8px;display:flex;align-items:center;justify-content:center;gap:6px;white-space:nowrap}

/* nav */
.main-nav{left:0;top:62px;width:784px;height:22px;background:var(--black)}
.nav-item{position:absolute;top:0;height:22px;line-height:22px;font-family:"Bitter",serif;font-size:7.5px;color:#fff;text-align:center;text-transform:uppercase;white-space:nowrap}
.nav-item.active{background:var(--gold)}
.nav-sep{position:absolute;top:7px;width:1px;height:8px;background:#555}

/* hero */
.hero{left:0;top:84px;width:784px;height:247px;background:linear-gradient(180deg,var(--hero-light),var(--hero-dark))}
.hero-photo{left:0;top:84px;width:260px;height:247px;background:linear-gradient(90deg,#c9b79a,#d9cbaa 70%,rgba(216,204,171,0))}
.hero-title{right:339px;top:176px;text-align:right;font-family:"Bitter",serif;font-size:21px;line-height:21px;color:var(--gold);white-space:nowrap}
.hero-sub{right:339px;top:225px;font-family:"Bitter",serif;font-size:10px;color:var(--ink);white-space:nowrap}

/* form */
.pickup-form{left:458px;top:54px;width:175px;height:232px;background:var(--gold);border-radius:0 0 4px 4px}
.pickup-form h2{position:absolute;left:0;top:9px;width:100%;text-align:center;font-family:"Bitter",serif;font-weight:400;font-size:13.5px;color:#fff;white-space:nowrap}
.form-label{position:absolute;left:8px;font-size:7.5px;color:#fff}
.field{position:absolute;height:17px;background:var(--field);border:1px solid #d8cfb9;font-size:5px;color:#999;padding-left:5px;line-height:15px}
.field.select{color:#333;font-weight:700}
.field.select::after{content:"";position:absolute;right:1px;top:1px;width:7px;height:13px;border-left:1px solid #ccc}
.submit{position:absolute;left:49px;top:194px;width:76px;height:18px;background:var(--black);color:#fff;font-size:7.5px;line-height:18px;text-align:center;border-radius:2px}

/* sections */
.welcome{left:0;top:331px;width:784px;height:157px;background:var(--cream)}
.section-title{position:absolute;left:0;width:784px;text-align:center;font-family:"Bitter",serif;font-weight:500;font-size:21px;color:var(--ink)}
.section-title .accent{color:var(--gold)}
.divider{position:absolute;left:223px;width:338px;height:1px}
.divider::before,.divider::after{content:"";position:absolute;top:0;width:147px;height:1px;background:var(--line)}
.divider::before{left:0}.divider::after{right:0}
.divider .dot{position:absolute;left:165px;top:-4px;width:8px;height:8px;border-radius:50%;background:var(--gold)}
.body-text{position:absolute;left:0;width:784px;text-align:center;font-size:6px;color:#333}
.body-text b{font-weight:700}
.read-more{left:366px;top:449px;width:52px;height:15px;background:var(--black);color:#fff;font-size:7px;line-height:15px;text-align:center;border-radius:2px}

.feature-label{position:absolute;font-size:7.5px;line-height:9.5px;color:var(--ink);white-space:nowrap}
.feature-label.right{text-align:right}

/* faq */
.faq-head{position:absolute;left:432px;top:804px;font-family:"Bitter",serif;font-size:21px;color:var(--gold)}
.faq-open{left:151px;top:873px;width:358px;height:58px;border:1px solid #ddd;border-radius:2px;background:#fff}
.faq-open .q{margin:1px;height:17px;background:var(--gold);color:#fff}
.q{font-size:6.2px;line-height:17px;padding-left:13px}
.faq-item{position:absolute;left:151px;width:358px;height:19px;border:1px solid #ddd;border-radius:2px;padding:1px;background:#fff}
.faq-item .q{background:var(--acc-bg);color:#333;height:15px;line-height:15px}

/* footer */
.site-footer{left:0;top:1126px;width:784px;height:74px;background:var(--footer)}
.foot-link{position:absolute;top:25px;font-family:"Bitter",serif;font-size:7.5px;color:var(--ink);white-space:nowrap}
.foot-link.active{color:var(--gold)}
.copyright{position:absolute;top:42px;left:0;width:784px;text-align:center;font-size:5.5px;color:#444}
</style>
</head>
<body>

<header class="site-header">
  <div class="abs brand">
    <span class="brand-mark"></span>
    <div class="brand-name">Harbor<br>Kindness<br>Fund</div>
  </div>
  <div class="abs call">
    <span class="call-icon"><svg width="9" height="9" viewBox="0 0 24 24"><path fill="#fff" d="M6.6 10.8a15 15 0 0 0 6.6 6.6l2.2-2.2c.3-.3.7-.4 1-.2 1.1.4 2.3.6 3.6.6.6 0 1 .4 1 1V20c0 .6-.4 1-1 1A17 17 0 0 1 3 4c0-.6.4-1 1-1h3.5c.6 0 1 .4 1 1 0 1.3.2 2.5.6 3.6.1.3 0 .7-.2 1z"/></svg></span>
    <span>Call :1-800-555-0142</span>
  </div>
  <div class="abs donate-btn">Donate Now
    <svg width="9" height="9" viewBox="0 0 10 10"><circle cx="5" cy="3" r="2.2" fill="#fff"/><path d="M1 10a4 4 0 0 1 8 0z" fill="#fff"/></svg>
  </div>
</header>

<nav class="abs main-nav">
  <div class="nav-item active" style="left:152px;width:58px">Home</div>
  <div class="nav-item" style="left:218px;width:60px">About Us</div>
  <div class="nav-sep" style="left:284px"></div>
  <div class="nav-item" style="left:292px;width:72px">Get Started</div>
  <div class="nav-sep" style="left:370px"></div>
  <div class="nav-item" style="left:378px;width:70px">Contact Us</div>
</nav>

<section class="abs hero"></section>
<div class="abs hero-photo" role="img" aria-label="Photo of three smiling children wearing caps and glasses"></div>
<div class="abs hero-title">Donate boat to<br>Charity!</div>
<div class="abs hero-sub">Your boat can make a difference!</div>

<form class="abs pickup-form">
  <h2>Donation Pick Up Form</h2>
  <div class="form-label" style="top:39px">Contact Information</div>
  <div class="field" style="left:8px;top:55px;width:75px">First Name</div>
  <div class="field" style="left:92px;top:55px;width:74px">Last Name</div>
  <div class="field" style="left:8px;top:78px;width:75px">Zip Code</div>
  <div class="field" style="left:92px;top:78px;width:74px">Day Phone</div>
  <div class="field" style="left:8px;top:101px;width:158px">Email Address</div>
  <div class="form-label" style="top:123px">Auto Donation Information</div>
  <div class="field select" style="left:8px;top:142px;width:75px">Choose Year</div>
  <div class="field select" style="left:92px;top:142px;width:74px">Choose Make</div>
  <div class="field" style="left:8px;top:167px;width:158px">Model of Vehicle</div>
  <div class="submit">Submit Application</div>
</form>

<section class="abs welcome">
  <h1 class="section-title" style="top:23px">WELCOME TO <span class="accent">HKF</span></h1>
  <div class="divider" style="top:64px"><span class="dot"></span></div>
  <p class="body-text" style="top:81px"><b>Harbor Kindness Fund's</b> mission is to improve, empower and to bring joy to the lives of children and their families affected by cancer.</p>
  <p class="body-text" style="top:99px"><b style="color:var(--gold)">HKF</b> adapts its support to fit each child's needs; from education to assistance with treatment, recovery and family support.</p>
</section>
<div class="abs read-more">Read More</div>

<h2 class="section-title" style="top:509px">DONATE BOAT TO <span class="accent">CHARITY!</span></h2>
<div class="section-title serif" style="top:536px;font-size:10px;font-weight:500">Your boat can make a difference!</div>
<div class="divider" style="top:565px"><span class="dot"></span></div>

<svg class="abs" style="left:0;top:560px" width="784" height="220" viewBox="0 560 784 220">
  <g stroke="#777" stroke-width="1">
    <line x1="308" y1="599" x2="345" y2="623"/><line x1="285" y1="666" x2="327" y2="667"/><line x1="308" y1="734" x2="345" y2="711"/>
    <line x1="475" y1="599" x2="439" y2="623"/><line x1="498" y1="666" x2="457" y2="667"/><line x1="475" y1="734" x2="439" y2="711"/>
  </g>
  <circle cx="392" cy="667" r="65" fill="#fff" stroke="#999" stroke-dasharray="1.5 2"/>
  <text x="392" y="674" text-anchor="middle" font-family="Bitter, serif" font-size="20" font-weight="700" fill="#9a7f48">HKF</text>
  <g fill="#d9cdb0" stroke="#8d8d8d" stroke-width="1">
    <circle cx="345" cy="623" r="3.5"/><circle cx="327" cy="667" r="3.5"/><circle cx="345" cy="711" r="3.5"/>
    <circle cx="439" cy="623" r="3.5"/><circle cx="457" cy="667" r="3.5"/><circle cx="439" cy="711" r="3.5"/>
  </g>
  <g fill="#111" stroke="#ddd" stroke-width="2.5">
    <circle cx="308" cy="599" r="20"/><circle cx="285" cy="666" r="20"/><circle cx="308" cy="734" r="20"/>
    <circle cx="475" cy="599" r="20"/><circle cx="498" cy="666" r="20"/><circle cx="475" cy="734" r="20"/>
  </g>
  <g fill="#fff">
    <path d="M307 587v17h-9zM309 589l8 15h-8z"/><path d="M296 606h24l-3 4h-18z"/>
    <path d="M284 654v17h-9zM286 657l8 14h-8z"/><path d="M273 673h24l-3 4h-18z"/>
    <text x="475" y="608" text-anchor="middle" font-family="Lato, sans-serif" font-weight="700" font-size="22">✓</text>
    <rect x="489" y="662" width="18" height="12" rx="1"/><rect x="487" y="658" width="22" height="4" fill="#fff"/>
    <text x="475" y="743" text-anchor="middle" font-family="Lato, sans-serif" font-weight="700" font-size="24">$</text>
  </g>
  <circle cx="308" cy="734" r="10" fill="none" stroke="#fff" stroke-width="2"/>
  <line x1="301" y1="741" x2="315" y2="727" stroke="#fff" stroke-width="2"/>
  <rect x="497" y="663" width="2" height="11" fill="#111"/>
</svg>
<div class="feature-label right" style="left:180px;top:591px;width:100px">Free Towing In<br>24-48 Hours</div>
<div class="feature-label right" style="left:157px;top:658px;width:100px">We Accept<br>All Boats</div>
<div class="feature-label right" style="left:170px;top:726px;width:110px">Boat Will Be Sold on the<br>Largest Auction Network</div>
<div class="feature-label" style="left:504px;top:591px">Boat Donations Help Fund<br>Charitable Programs</div>
<div class="feature-label" style="left:527px;top:658px">Hassle<br>Free Donation</div>
<div class="feature-label" style="left:504px;top:726px">Income<br>Tax Deduction</div>

<h2 class="faq-head">Questions</h2>
<div class="divider" style="top:845px"><span class="dot"></span></div>
<div class="abs faq-open"><div class="q">What types of vehicles can be donated?</div></div>
<div class="faq-item" style="top:940px"><div class="q">What paperwork do I need to donate my vehicle?</div></div>
<div class="faq-item" style="top:968px"><div class="q">Is my donated vehicle tax-deductible?</div></div>
<div class="faq-item" style="top:997px"><div class="q">What if the vehicle is not registered in my name?</div></div>
<div class="faq-item" style="top:1025px"><div class="q">How much will I receive as a tax deduction for my vehicle?</div></div>
<div class="faq-item" style="top:1054px"><div class="q">When will I receive my tax receipt?</div></div>
<div class="faq-item" style="top:1082px"><div class="q">How do I schedule a pick up?</div></div>

<footer class="abs site-footer">
  <span class="foot-link active" style="left:257px">HOME</span>
  <span class="foot-link" style="left:318px">ABOUT US</span>
  <span class="foot-link" style="left:394px">GET STARTED</span>
  <span class="foot-link" style="left:481px">CONTACT US</span>
  <p class="copyright">Copyright 2017 Harbor Kindness Fund. All Rights Reserved.</p>
</footer>

</body>
</html>
```